Business Card Design Project

I need a business card for a Management Consultancy. We work with organisational design and development and strategic change using facilitation, consulting and coaching.

Size of card is 90 x 55mm.

Logo is attached.

Wording is:

Maria Kestle
Director

tel 0491627358
email is: info@tallowpoint.com.au

Target Market(s)

Government departments and not for profit organisations mainly.

Industry/Entity Type

Business

Requirements
Must have
• White or colour background not black.

On one side of the card, either back or front please include the words:

Leading Strategic Change

Two sided business card

```html
<!DOCTYPE html>
<html lang="en">
<head>
<meta charset="utf-8">
<title>TallowPoint – Business Card</title>
<link rel="stylesheet" href="https://fonts.googleapis.com/css2?family=Open+Sans:wght@400;600&family=Arimo:wght@400&display=swap">
<style>
  :root {
    --backdrop: #5f6266;
    --backdrop-dark: #3b3d40;
    --card-white: #ffffff;
    --brand-blue: #3a7db4;
    --brand-blue-light: #6aa6cf;
    --brand-blue-deep: #2f6fa6;
    --slate: #5b6573;
    --text-grey: #4a4a4a;
    --accent-green: #7cc142;
    --mark-grey: #9aa6b2;
  }
  * { margin: 0; padding: 0; box-sizing: border-box; }
  html, body {
    width: 1200px; height: 700px; overflow: hidden;
  }
  body {
    background: radial-gradient(ellipse at 50% 40%, var(--backdrop), var(--backdrop-dark));
    font-family: "Open Sans", sans-serif;
    position: relative;
  }
  .card {
    position: absolute;
    top: 212px;
    width: 450px;
    height: 275px;
    overflow: hidden;
    box-shadow: 0 14px 30px rgba(0,0,0,0.4);
  }

  /* Back side */
  .card-back {
    left: 120px;
    background: linear-gradient(135deg, var(--brand-blue-deep) 0%, var(--brand-blue) 45%, var(--brand-blue-light) 100%);
  }
  .card-back .corner-mark {
    position: absolute;
    left: -40px; top: -70px;
    width: 220px; height: 220px;
    border-radius: 50%;
    background: radial-gradient(circle at 60% 60%, #c9d3dc, var(--mark-grey));
  }
  .card-back .brand-name {
    position: absolute;
    left: 196px; top: 34px;
    font-weight: 600;
    font-size: 22px;
    color: var(--card-white);
  }
  .card-back .tagline {
    position: absolute;
    right: 34px; bottom: 40px;
    font-family: "Arimo", sans-serif;
    font-size: 15px;
    color: var(--card-white);
    letter-spacing: 0.2px;
  }

  /* Front side */
  .card-front {
    left: 630px;
    background: var(--card-white);
  }
  .brand {
    position: absolute;
    left: 26px; top: 28px;
    display: flex; align-items: center; gap: 10px;
  }
  .brand-dot {
    width: 42px; height: 42px; border-radius: 50%;
    background: radial-gradient(circle at 40% 40%, #cfd8e0, var(--mark-grey));
  }
  .brand-word {
    font-weight: 600;
    font-size: 24px;
    color: var(--slate);
  }
  .person {
    position: absolute;
    left: 26px; top: 126px;
  }
  .person-name {
    font-weight: 600;
    font-size: 15px;
    color: var(--text-grey);
    line-height: 1.2;
  }
  .person-role {
    font-size: 10px;
    color: var(--text-grey);
  }
  .divider {
    position: absolute;
    left: 96px; top: 164px;
    width: 300px; height: 1px;
    background: var(--brand-blue);
  }
  .contact {
    position: absolute;
    left: 26px; top: 172px;
    list-style: none;
    font-size: 11px;
    color: var(--text-grey);
  }
  .contact li {
    display: flex; align-items: center; gap: 7px;
    margin-bottom: 3px;
  }
  .contact svg { width: 10px; height: 10px; flex: none; }
  .web-band {
    position: absolute;
    right: 0; bottom: 0;
    width: 220px; height: 30px;
    background: var(--brand-blue-deep);
    clip-path: polygon(8% 0, 100% 0, 100% 100%, 0 100%);
    display: flex; align-items: center; justify-content: flex-end;
    padding-right: 18px;
    font-size: 12px;
    color: var(--card-white);
  }
</style>
</head>
<body>

  <section class="card card-back" aria-label="Business card, back">
    <div class="corner-mark"></div>
    <p class="brand-name">TallowPoint</p>
    <p class="tagline">Leading Strategic Change...</p>
  </section>

  <section class="card card-front" aria-label="Business card, front">
    <div class="brand">
      <div class="brand-dot"></div>
      <span class="brand-word">TallowPoint</span>
    </div>

    <div class="person">
      <p class="person-name">Maria Kestle</p>
      <p class="person-role">Director</p>
    </div>
    <div class="divider"></div>

    <ul class="contact">
      <li>
        <svg viewBox="0 0 10 10" aria-hidden="true"><path d="M2 0.5 L3.6 2.6 L2.8 3.6 Q4 6 6.4 7.2 L7.4 6.4 L9.5 8 L8.2 9.5 Q3.5 9 0.5 1.8 Z" fill="var(--accent-green)"/></svg>
        <span>0491627358</span>
      </li>
      <li>
        <svg viewBox="0 0 10 10" aria-hidden="true"><rect x="0.5" y="2" width="9" height="6.5" fill="var(--accent-green)"/><path d="M0.8 2.3 L5 5.6 L9.2 2.3" stroke="#fff" stroke-width="0.9" fill="none"/></svg>
        <span>info@tallowpoint.com.au</span>
      </li>
    </ul>

    <div class="web-band">www.tallowpoint.com.au</div>
  </section>

</body>
</html>
```